Home inspection business! professional look attracting customers just by looks. Read must haves

its a new business I started on my own for home inspections I would like something very professional to give to real estate agents and clients, its going to have my license number on it my business phone number my name my website as well etc on the back side it will be servicing areas and also what kind of services I offer I also have a business card from someone else the way I would like mine to be. I will attach my logo

Home Inspection

listed in nice to haves

• phone number - 555 293 8471
• website- hollowpinecheck.com
• license number #2938475610
• my name Gavin keropulis
• picture of my logo and me on the front
• on the back of the card. stating I am servicing All of New York and Long Island
• also services I will offer will be home inspection -mold inspection -lead inspection -radon inspection -Termite Inspection -Infared Scan.
• and also we provide inspections for single family homes condos co-ops town-homes
• and commercial property
• same colors as the logos and also if you recommend fonts to look like the logo not sure up to you

```html
<!DOCTYPE html>
<html lang="en">
<head>
<meta charset="utf-8">
<title>Hollow Pine Check – Business Cards</title>
<link href="https://fonts.googleapis.com/css2?family=Poppins:wght@400;500&family=Montserrat:wght@500;600&display=swap" rel="stylesheet">
<style>
  :root {
    --stage: #3a3a3c;
    --card-white: #ffffff;
    --card-black: #0c0c0d;
    --brand-blue: #4a9ad9;
    --brand-grey: #6d6e71;
    --text-light: #f2f2f2;
    --text-dark: #5a5b5e;
  }
  * { margin: 0; padding: 0; box-sizing: border-box; }
  html, body {
    width: 1200px; height: 896px; overflow: hidden;
    background: var(--stage);
  }
  .stage {
    width: 1200px; height: 896px;
    display: flex; align-items: center; justify-content: center; gap: 40px;
  }
  .card {
    position: relative;
    width: 540px; height: 309px;
    border-radius: 18px;
    overflow: hidden;
    box-shadow: 0 10px 30px rgba(0,0,0,.35);
  }

  /* Back side */
  .card--back {
    background: var(--card-black);
    color: var(--text-light);
    display: flex; flex-direction: column; align-items: center;
    padding-top: 46px;
  }
  .brand { display: flex; flex-direction: column; align-items: center; }
  .brand__name {
    display: flex; align-items: center; gap: 10px;
    font-family: "Montserrat", sans-serif; font-weight: 600;
    font-size: 27px; letter-spacing: .5px;
  }
  .brand__dot { width: 14px; height: 14px; border-radius: 50%; }
  .brand__tag {
    font-family: "Montserrat", sans-serif; font-weight: 500;
    font-size: 12px; letter-spacing: 7px; margin-top: 4px;
  }
  .card--back .brand__name { color: var(--text-light); }
  .card--back .brand__dot { background: var(--brand-blue); }
  .card--back .brand__tag { color: var(--text-light); }
  .services {
    margin-top: 26px;
    font-family: "Poppins", sans-serif; font-size: 13.5px;
    line-height: 1.62; text-align: center;
  }

  /* Front side */
  .card--front { background: var(--card-white); }
  .card--front .brand {
    position: absolute; top: 34px; right: 40px; align-items: flex-start;
  }
  .card--front .brand__name { color: var(--brand-grey); font-size: 25px; }
  .card--front .brand__dot { background: var(--brand-blue); }
  .card--front .brand__tag { color: var(--brand-grey); font-size: 11px; letter-spacing: 6.5px; }
  .rule-top {
    position: absolute; top: 112px; left: 230px; right: 40px;
    height: 1px; background: var(--brand-blue);
  }
  .holder-tab {
    position: absolute; left: 0; top: 152px;
    width: 10px; height: 44px; background: var(--brand-blue);
  }
  .holder {
    position: absolute; left: 36px; top: 150px; right: 40px;
    font-family: "Poppins", sans-serif;
  }
  .holder__name {
    color: var(--brand-blue); font-weight: 500; font-size: 20px;
    letter-spacing: .5px; text-transform: uppercase;
    border-bottom: 1px solid var(--brand-blue);
    padding-bottom: 2px; display: block;
  }
  .holder__role { color: var(--text-dark); font-size: 13px; margin-top: 2px; }
  .contacts {
    list-style: none; margin-top: 12px;
    font-size: 13px; color: var(--text-dark); line-height: 1.55;
  }
  .contacts li { display: flex; align-items: center; gap: 8px; }
  .contacts svg { width: 11px; height: 11px; flex: none; }
</style>
</head>
<body>
<main class="stage">

  <section class="card card--back" aria-label="Card back">
    <div class="brand">
      <div class="brand__name"><span class="brand__dot"></span>HOLLOW PINE CHECK</div>
      <div class="brand__tag">HOME INSPECTORS</div>
    </div>
    <p class="services">
      stating I am servicing All of New York and Long Island<br>
      also services I will offer will be home inspection<br>
      mold inspection -lead inspection -radon inspection<br>
      Termite Inspection -Infared Scan.<br>
      and also we provide inspections for single family<br>
      homes condos co-ops town-homes and commercial property
    </p>
  </section>

  <section class="card card--front" aria-label="Card front">
    <div class="brand">
      <div class="brand__name"><span class="brand__dot"></span>HOLLOW PINE CHECK</div>
      <div class="brand__tag">HOME INSPECTORS</div>
    </div>
    <div class="rule-top"></div>
    <div class="holder-tab"></div>
    <div class="holder">
      <span class="holder__name">Gavin Keropulis</span>
      <div class="holder__role">Director</div>
      <ul class="contacts">
        <li>#2938475610</li>
        <li>
          <svg viewBox="0 0 12 12" aria-hidden="true"><path d="M3 1 L5 3.5 L4 5 Q5 7 7 8 L8.5 7 L11 9 L10 11 Q4 11 1 2 Z" fill="var(--brand-blue)"/></svg>
          555 293 8471
        </li>
        <li>
          <svg viewBox="0 0 12 12" aria-hidden="true"><rect x="1" y="2.5" width="10" height="7" rx="1" fill="none" stroke="var(--brand-blue)" stroke-width="1.3"/><path d="M1.5 3 L6 6.5 L10.5 3" fill="none" stroke="var(--brand-blue)" stroke-width="1.3"/></svg>
          info@hollowpinecheck.com
        </li>
        <li>
          <svg viewBox="0 0 12 12" aria-hidden="true"><circle cx="6" cy="6" r="5" fill="none" stroke="var(--brand-blue)" stroke-width="1.2"/><ellipse cx="6" cy="6" rx="2.2" ry="5" fill="none" stroke="var(--brand-blue)" stroke-width="1"/><line x1="1" y1="6" x2="11" y2="6" stroke="var(--brand-blue)" stroke-width="1"/></svg>
          www.hollowpinecheck.com
        </li>
      </ul>
    </div>
  </section>

</main>
</body>
</html>
```